Multi brand diverse distributor requires new business card

We're a distributor representing multiple brands and would like a new business card reflecting our diversity.

We incorporate landscape architecture, environmental engineering and sustainability into construction projects.

KV Group is the company name, and therefore the KV logo should be the primary logo.

Target Market(s)

Engineers, Landscape Architects, Environmental

Contact Information for Business Card

See sample

Colors

Designer to choose colors to be used in the design.

```html
<!DOCTYPE html>
<html lang="en">
<head>
<meta charset="UTF-8">
<title>KV Group – Business Card</title>
<link href="https://fonts.googleapis.com/css2?family=Open+Sans:wght@400;600;700&display=swap" rel="stylesheet">
<style>
  :root {
    --crimson: #c41e45;
    --ink: #1b1b1b;
    --paper: #ffffff;
    --grey-text: #4a4a4a;
    --stage: #cfcfcf;
  }
  * { margin: 0; padding: 0; box-sizing: border-box; }
  html, body { width: 1200px; height: 900px; overflow: hidden; }
  body {
    background: var(--stage);
    font-family: "Open Sans", Arial, sans-serif;
    position: relative;
  }
  .card {
    position: absolute;
    left: 340px;
    width: 520px;
    height: 300px;
    box-shadow: 0 8px 24px rgba(0,0,0,0.25);
  }
  .card--front { top: 120px; background: var(--paper); }
  .card--back { top: 470px; background: var(--ink); }

  /* front */
  .front-brand {
    position: absolute; top: 30px; right: 36px;
    display: flex; align-items: center; gap: 8px;
  }
  .front-brand__mark {
    width: 12px; height: 12px; background: var(--crimson);
  }
  .front-brand__name {
    color: var(--crimson);
    font-size: 20px;
    font-weight: 700;
  }
  .person { position: absolute; top: 100px; left: 150px; }
  .person__name { color: var(--crimson); font-size: 24px; font-weight: 400; line-height: 1.2; }
  .person__name strong { font-weight: 700; }
  .person__title { color: var(--grey-text); font-size: 12px; margin-left: 70px; }

  .contact { position: absolute; font-size: 13px; color: var(--ink); }
  .contact__row { display: flex; align-items: center; gap: 6px; line-height: 20px; }
  .contact__row svg { width: 12px; height: 12px; fill: var(--crimson); flex: none; }
  .contact--phones { top: 190px; left: 40px; font-size: 15px; }
  .contact--web { top: 158px; left: 330px; }

  .offices {
    position: absolute; bottom: 26px; left: 40px;
    display: flex; align-items: center; gap: 6px; font-size: 13px; color: var(--ink);
  }
  .offices svg { width: 12px; height: 14px; fill: var(--crimson); }
  .offices .sep { color: var(--crimson); margin: 0 3px; }

  /* back */
  .back-brand {
    position: absolute; top: 0; left: 0; right: 0; bottom: 0;
    display: flex; align-items: center; justify-content: center; gap: 14px;
  }
  .back-brand__mark {
    width: 22px; height: 22px; background: var(--crimson);
  }
  .back-brand__name {
    color: var(--paper); font-size: 36px; font-weight: 700;
  }
</style>
</head>
<body>

<section class="card card--front" aria-label="Business card front">
  <div class="front-brand">
    <span class="front-brand__mark"></span>
    <span class="front-brand__name">KV Group</span>
  </div>

  <div class="person">
    <div class="person__name"><strong>Marco</strong> Bellandi</div>
    <div class="person__title">B.Eng (Civil)</div>
  </div>

  <div class="contact contact--phones">
    <div class="contact__row">
      <svg viewBox="0 0 12 12"><path d="M3 0h6a1 1 0 0 1 1 1v10a1 1 0 0 1-1 1H3a1 1 0 0 1-1-1V1a1 1 0 0 1 1-1zm0 1.5v8h6v-8z"/></svg>
      <span>0400 217 364</span>
    </div>
    <div class="contact__row">
      <svg viewBox="0 0 12 12"><path d="M2.5 0.5l2 2.5-1.2 1.2a7 7 0 0 0 4.5 4.5L9 7.5l2.5 2-1.5 2C5 11.5 0.5 7 0.5 2z"/></svg>
      <span>1300 482 905</span>
    </div>
  </div>

  <div class="contact contact--web">
    <div class="contact__row">
      <svg viewBox="0 0 12 12"><path d="M0 2h12v8H0zm1 1v.5l5 3.5 5-3.5V3z"/></svg>
      <span>marco@kv.com.au</span>
    </div>
    <div class="contact__row">
      <svg viewBox="0 0 12 12"><circle cx="6" cy="6" r="6"/></svg>
      <span>www.kv.com.au</span>
    </div>
  </div>

  <div class="offices">
    <svg viewBox="0 0 12 14"><path d="M6 0a5 5 0 0 1 5 5c0 3.5-5 9-5 9S1 8.5 1 5a5 5 0 0 1 5-5zm0 3a2 2 0 1 0 0 4 2 2 0 0 0 0-4z"/></svg>
    <span>Adelaide</span><span class="sep">|</span>
    <span>Brisbane</span><span class="sep">|</span>
    <span>Melbourne</span><span class="sep">|</span>
    <span>Perth</span><span class="sep">|</span>
    <span>Sydney</span>
  </div>
</section>

<section class="card card--back" aria-label="Business card back">
  <div class="back-brand">
    <span class="back-brand__mark"></span>
    <span class="back-brand__name">KV Group</span>
  </div>
</section>

</body>
</html>
```